Halvorn Hire Business Card Design

Need business cards designed for our new equipment rental. We specialize in renting to landscape / tree professionals, contractors, Do-It-Yourself'ers and Around the home or office. Looking for a eye catching card. Landscape and construction should be the theme. The logo is attached, and you can see our colors from the logo. You can use whatever color goes with it ok.

Target Market(s)

First off Landscape and Tree Professional. Then contractors, Do-It-Yourself'ers and rentals for Around the home or office.

Industry/Entity Type

Business

Contact Information for Business Card

Eye catching background that blends landscaping with construction equipment

Requirements
Must have
• Name on Card will Be: Derek Pollard (Manager)
• My Direct Phone Number is: 352-418-7093
• derek@halvornhire.example
• www.halvornhire.example
• 4172 Wexley Mill Road,
• Dade City FL 33590
Nice to have
• Would be Nice to have these bullets on the Face of the card that does not have all my information.
• Serving:
• Landscape / Tree Professionals
• Contractors
• DYI'ers or say Do-It-Yourself'ers
• Maybe have serving small and centered above these bullets, and these 3 bullets along the bottom of the card. Ideas?

```html
<!DOCTYPE html>
<html lang="en">
<head>
<meta charset="utf-8">
<title>Halvorn Hire – Business Card</title>
<link rel="stylesheet" href="https://fonts.googleapis.com/css2?family=Chakra+Petch:wght@500;600;700&family=Roboto:wght@400&display=swap">
<style>
  :root {
    --backdrop: #2b2b2b;
    --card-light: #f1f1f1;
    --navy: #023c63;
    --ink-grey: #555555;
    --title-grey: #8f8f8f;
    --accent: #f6b56a;
    --white: #ffffff;
  }
  * { margin: 0; padding: 0; box-sizing: border-box; }
  html, body { width: 1200px; height: 960px; overflow: hidden; }
  body {
    background: var(--backdrop);
    position: relative;
    font-family: "Chakra Petch", sans-serif;
  }
  .card {
    position: absolute;
    width: 600px;
    height: 343px;
    overflow: hidden;
  }
  .card-front { left: 314px; top: 113px; background: var(--card-light); }
  .card-back { left: 311px; top: 472px; background: var(--navy); }

  .scene-fill {
    position: absolute;
    right: 0; top: 0;
    width: 280px; height: 343px;
    background: linear-gradient(200deg, rgba(200,200,200,0.55) 0%, rgba(220,220,220,0.25) 55%, rgba(241,241,241,0) 100%);
  }

  .brand-name {
    position: absolute;
    font-family: "Chakra Petch", sans-serif;
    font-weight: 700;
    letter-spacing: 1px;
    white-space: nowrap;
  }
  .card-front .brand-name {
    left: 30px; top: 96px;
    font-size: 38px;
    color: var(--navy);
  }
  .card-back .brand-name {
    left: 0; right: 0; top: 112px;
    text-align: center;
    font-size: 50px;
    color: var(--white);
  }

  .address {
    position: absolute;
    left: 31px; top: 182px;
    font-size: 14px; font-weight: 600; line-height: 18px;
    font-style: normal;
    color: var(--ink-grey);
  }
  .contact-list {
    position: absolute;
    left: 31px; top: 236px;
    list-style: none;
  }
  .contact-list li {
    display: flex; align-items: center;
    height: 20px;
    font-size: 14px; font-weight: 600;
    color: var(--ink-grey);
  }
  .contact-list svg { width: 14px; height: 14px; margin-right: 8px; fill: var(--navy); flex: none; }

  .person {
    position: absolute;
    right: 30px; top: 229px;
    text-align: right;
  }
  .person-name {
    font-size: 22px; font-weight: 700; letter-spacing: 1.5px;
    color: var(--navy); line-height: 26px;
  }
  .person-title {
    font-size: 16px; font-weight: 700; letter-spacing: 1.5px;
    color: var(--title-grey); line-height: 20px;
  }

  .serving-label {
    position: absolute;
    left: 0; right: 0; top: 212px;
    text-align: center;
    font-size: 12px; font-weight: 600; letter-spacing: 3px;
    color: var(--accent);
  }
  .serving-list {
    position: absolute;
    left: 0; right: 0; top: 236px;
    display: flex; justify-content: center; gap: 22px;
    list-style: none;
  }
  .serving-list li {
    display: flex; align-items: center;
    font-size: 13px; font-weight: 600;
    color: var(--white);
    white-space: nowrap;
  }
  .serving-list li::before {
    content: "";
    width: 6px; height: 6px;
    margin-right: 7px;
    border-radius: 50%;
    background: var(--accent);
  }

  .back-web {
    position: absolute;
    left: 0; right: 0; top: 294px;
    text-align: center;
    font-family: "Roboto", sans-serif;
    font-size: 14px; letter-spacing: 4.2px;
    color: var(--white);
  }
</style>
</head>
<body>

<section class="card card-front">
  <div class="scene-fill" role="img" aria-label="Faint landscape and construction equipment scene"></div>

  <div class="brand-name">HALVORN HIRE</div>

  <address class="address">
    4172 Wexley Mill Road,<br>
    Dade City FL 33590
  </address>

  <ul class="contact-list">
    <li>
      <svg viewBox="0 0 16 16" aria-hidden="true"><path d="M3.6 1.2l2.3 2.6-1.4 2a9 9 0 0 0 5.7 5.7l2-1.4 2.6 2.3-1.5 2.1C7.2 14.6 1.4 8.8 1.5 2.7z"/></svg>
      352-418-7093
    </li>
    <li>
      <svg viewBox="0 0 16 16" aria-hidden="true"><path d="M1 4h14v9H1zM2.5 5.2v0.4L8 9.2l5.5-3.6v-0.4z"/></svg>
      derek@halvornhire.example
    </li>
    <li>
      <svg viewBox="0 0 16 16" aria-hidden="true"><path d="M8 1a7 7 0 1 0 0 14A7 7 0 1 0 8 1zM5 4.2c1.3 0.3 2.2 1.2 1.8 2.3-0.4 1 0.9 1.4 1.6 2.3 0.6 0.9-0.4 2.3-1 3.6-1.7-0.6-1.5-2.4-2.6-3.3-1-0.8-2.2-0.7-2.4-1.8A5.6 5.6 0 0 1 5 4.2zM10.2 3.3a5.6 5.6 0 0 1 3.1 5.5c-0.9-0.2-1.4-1.1-2.3-1-1 0.1-1.6-1.2-0.8-2.2z"/></svg>
      www.halvornhire.example
    </li>
  </ul>

  <div class="person">
    <div class="person-name">DEREK POLLARD</div>
    <div class="person-title">MANAGER</div>
  </div>
</section>

<section class="card card-back">
  <div class="brand-name">HALVORN HIRE</div>
  <div class="serving-label">SERVING</div>
  <ul class="serving-list">
    <li>Landscape / Tree Professionals</li>
    <li>Contractors</li>
    <li>Do-It-Yourself'ers</li>
  </ul>
  <div class="back-web">www.halvornhire.example</div>
</section>

</body>
</html>
```